Dorsey K. Wendell Business Card

We need a business card for our company Dorsey K. Wendell Heating & Plumbing to be distributed to potential customers. It should follow the color scheme of our logo and have a modern upscale and masculine look.

The logo is attached and the info below should also be included:

5187 W. Cedar Brook Rd.
Manheim, PA 17545

Russell T. Wendell
(717) 592-0817
russelltwendell@fernmail.net
dorseykwendell.net
PA #093148

Industry/Entity Type

Business

Contact Information for Business Card

5187 W. Cedar Brook Rd.
Manheim, PA 17545

Russell T. Wendell
(717) 592-0817
russelltwendell@fernmail.net
dorseykwendell.net
PA #093148

Colors

Designer to choose colors to be used in the design.

Requirements
Must have
• Information above included

```html
<!DOCTYPE html>
<html lang="en">
<head>
<meta charset="utf-8">
<title>Dorsey K. Wendell Business Card</title>
<link href="https://fonts.googleapis.com/css2?family=Archivo:wght@800&family=Source+Sans+3:wght@400&display=swap" rel="stylesheet">
<style>
  :root {
    --backdrop: #616161;
    --card-green: #aecf37;
    --card-green-deep: #9dbf3f;
    --brand-blue: #0f57a8;
    --white: #ffffff;
  }
  * { margin: 0; padding: 0; box-sizing: border-box; }
  html, body { width: 1200px; height: 1000px; overflow: hidden; }
  body { background: var(--backdrop); position: relative; font-family: "Source Sans 3", Arial, sans-serif; }

  .card { position: absolute; left: 404px; width: 397px; height: 226px; background: var(--card-green); overflow: hidden; }
  .card--front { top: 261px; }
  .card--back { top: 516px; }

  .brand-name { font-family: "Archivo", Arial, sans-serif; font-weight: 800; text-transform: uppercase; line-height: 1; white-space: nowrap; }

  /* Front */
  .front-mark { position: absolute; left: 80px; top: 82px; width: 54px; height: 60px; background: var(--brand-blue); }
  .front-name { position: absolute; left: 144px; top: 97px; color: var(--white); }
  .front-name .brand-line-main { display: block; font-size: 17px; letter-spacing: 0.3px; }
  .front-name .brand-line-sub { display: block; font-size: 8.5px; letter-spacing: 0.9px; margin-top: 7px; text-align: right; }

  /* Back */
  .back-name { position: absolute; right: 20px; top: 18px; text-align: right; color: var(--brand-blue); }
  .back-name .brand-line-main { display: block; font-size: 15px; }
  .back-name .brand-line-sub { display: block; font-size: 6.5px; letter-spacing: 0.6px; margin-top: 4px; }
  .person-name { position: absolute; right: 20px; top: 56px; font-family: "Archivo", Arial, sans-serif; font-weight: 800; font-size: 12px; font-variant: small-caps; letter-spacing: 1px; color: var(--brand-blue); white-space: nowrap; }
  .address { position: absolute; right: 20px; top: 76px; font-style: normal; font-size: 10px; line-height: 12px; text-align: right; color: var(--brand-blue); white-space: nowrap; }

  .contact-tab { position: absolute; left: 0; top: 71px; width: 94px; height: 19px; background: var(--brand-blue); color: var(--white); font-size: 12px; line-height: 19px; padding-left: 35px; letter-spacing: -0.2px; }

  .contact-list { position: absolute; left: 35px; top: 103px; list-style: none; }
  .contact-item { display: flex; align-items: center; height: 15px; margin-bottom: 15.7px; color: var(--brand-blue); font-size: 11.5px; white-space: nowrap; }
  .contact-item svg { width: 15px; height: 15px; margin-right: 8px; flex: none; }

  .corner-block { position: absolute; left: 289px; top: 120px; width: 108px; height: 106px; background: var(--card-green-deep); }
</style>
</head>
<body>
  <section class="card card--front" aria-label="Card front">
    <div class="front-mark"></div>
    <div class="front-name brand-name">
      <span class="brand-line-main">Dorsey K. Wendell</span>
      <span class="brand-line-sub">Heating &amp; Plumbing</span>
    </div>
  </section>

  <section class="card card--back" aria-label="Card back">
    <div class="corner-block"></div>
    <div class="back-name brand-name">
      <span class="brand-line-main">Dorsey K. Wendell</span>
      <span class="brand-line-sub">Heating &amp; Plumbing</span>
    </div>
    <div class="person-name">Russell T. Wendell</div>
    <address class="address">5187 W. Cedar Brook Rd.<br>Manheim, PA 17545</address>

    <div class="contact-tab">CONTACT</div>

    <ul class="contact-list">
      <li class="contact-item">
        <svg viewBox="0 0 15 15" aria-hidden="true"><rect x="0.75" y="0.75" width="13.5" height="13.5" fill="none" stroke="#0f57a8" stroke-width="1.5"/><rect x="3" y="4.5" width="9" height="6" fill="#0f57a8"/><path d="M3 4.5 L7.5 8 L12 4.5" fill="none" stroke="#aecf37" stroke-width="1"/></svg>
        russelltwendell@fernmail.net
      </li>
      <li class="contact-item">
        <svg viewBox="0 0 15 15" aria-hidden="true"><rect x="0.75" y="0.75" width="13.5" height="13.5" fill="none" stroke="#0f57a8" stroke-width="1.5"/><circle cx="7.5" cy="7.5" r="4.5" fill="#0f57a8"/><path d="M3 7.5 H12 M7.5 3 V12" stroke="#aecf37" stroke-width="0.8"/></svg>
        dorseykwendell.net
      </li>
      <li class="contact-item">
        <svg viewBox="0 0 15 15" aria-hidden="true"><rect x="0.75" y="0.75" width="13.5" height="13.5" fill="none" stroke="#0f57a8" stroke-width="1.5"/><path d="M4.5 3.5 L6 3.5 L6.5 5.5 L5.5 6.3 Q6.6 8.6 8.7 9.5 L9.5 8.5 L11.5 9 L11.5 10.5 Q11 11.5 9.5 11.5 Q4 10.5 3.5 5 Q3.5 3.8 4.5 3.5 Z" fill="#0f57a8"/></svg>
        (717) 592-0817
      </li>
      <li class="contact-item">
        <svg viewBox="0 0 15 15" aria-hidden="true"><rect x="0.75" y="0.75" width="13.5" height="13.5" fill="none" stroke="#0f57a8" stroke-width="1.5"/><circle cx="7.5" cy="5.3" r="2.2" fill="#0f57a8"/><path d="M3.5 12 Q3.5 8 7.5 8 Q11.5 8 11.5 12 Z" fill="#0f57a8"/></svg>
        PA #093148
      </li>
    </ul>
  </section>
</body>
</html>
```